Option Sheet

We need a one page option sheet with a left to right reading of the five options. It should be a one sheet, multiple colors and definitive separations between options This is used in a sales consultation. Backround or colors not in option need to have the follow RGB value (5 red, 20 green, 63 blue)

We added a smaller text file, please change that point

Target Market(s)

Divorce

Industry/Entity Type

Legal

Requirements
Must have
• 1) All five options left to right
• 2)language included in sheet

```html
<!DOCTYPE html>
<html lang="en">
<head>
<meta charset="utf-8">
<title>Divorce – Five Options</title>
<link rel="stylesheet" href="https://fonts.googleapis.com/css2?family=Arimo:ital,wght@0,400;0,700;1,400;1,700&display=swap">
<style>
  :root {
    --page: rgb(5, 20, 63);
    --ink: #111111;
    --title-fill: #ffffff;
    --title-stroke: #4a4a4a;
    --blue: #7ccff3;
    --pink: #f083b2;
    --yellow: #fcf065;
    --green: #97c98a;
    --orange: #f9bf7c;
    --shadow: rgba(0, 0, 0, 0.6);
  }
  * { box-sizing: border-box; margin: 0; padding: 0; }
  html, body {
    width: 1200px; height: 848px; overflow: hidden;
    background: var(--page);
    font-family: "Arimo", Arial, sans-serif;
    color: var(--ink);
  }
  .sheet { position: relative; width: 1200px; height: 848px; background: var(--page); }

  .sheet-title {
    position: absolute; left: 145px; top: 50px;
    white-space: nowrap;
    font-weight: 700; font-size: 97px; line-height: 110px;
    color: var(--title-fill);
    -webkit-text-stroke: 1.6px var(--title-stroke);
    text-shadow: 4px 5px 5px rgba(0,0,0,0.5);
  }
  .sheet-title .sub {
    display: inline-block;
    font-style: italic; font-weight: 400; font-size: 92px;
    margin-left: 29px; letter-spacing: -1px;
    transform: scaleX(0.79); transform-origin: left center;
  }

  .option {
    position: absolute; top: 190px; height: 567px;
    padding: 10px 10px 0 16px;
    box-shadow: 5px 5px 4px var(--shadow);
    white-space: nowrap;
  }
  .option--nothing    { left: 41px;  width: 168px; background: var(--blue); }
  .option--counseling { left: 234px; width: 192px; background: var(--pink); top: 192px; }
  .option--diy        { left: 450px; width: 226px; background: var(--yellow); }
  .option--limited    { left: 700px; width: 272px; background: var(--green); }
  .option--hire       { left: 997px; width: 164px; background: var(--orange); top: 192px; }

  .option-number {
    text-align: center; font-style: italic; font-weight: 700;
    font-size: 22px; line-height: 24px; margin-left: -6px;
  }
  .option-name {
    text-align: center; font-weight: 700;
    font-size: 28px; line-height: 29px; margin: 5px 0 0 -6px;
  }
  .section-label {
    font-style: italic; font-weight: 700;
    font-size: 18px; line-height: 24px; margin-top: 7px;
  }
  .option-name + .section-label { margin-top: 9px; }
  .points { list-style: none; margin-bottom: 4px; }
  .points li {
    position: relative; padding-left: 19px;
    font-size: 18px; line-height: 22px; margin-top: 4px;
  }
  .points li::before {
    content: ""; position: absolute; left: 0; top: 5px;
    width: 11px; height: 11px; border-radius: 50%;
    border: 1.6px solid var(--ink);
    box-shadow: 1.5px 1.5px 0 var(--ink);
  }
</style>
</head>
<body>
<main class="sheet">
  <h1 class="sheet-title">DIVORCE<span class="sub">(Five Options)</span></h1>

  <section class="option option--nothing">
    <p class="option-number">Option #1:</p>
    <h2 class="option-name">Do Nothing</h2>
    <h3 class="section-label">Advantages:</h3>
    <ul class="points">
      <li>Stay married</li>
      <li>No life<br>Changes</li>
    </ul>
    <h3 class="section-label">Disadvantages:</h3>
    <ul class="points">
      <li>Remain<br>unhappy,<br>depressed,<br>anxious</li>
      <li>Money and<br>assets may<br>disappear</li>
      <li>What is going<br>to change?</li>
    </ul>
  </section>

  <section class="option option--counseling">
    <p class="option-number">Option #2:</p>
    <h2 class="option-name">Go to<br>Counseling</h2>
    <h3 class="section-label">Advantages:</h3>
    <ul class="points">
      <li>Reconcile<br>marriage</li>
      <li>Help make<br>a better life</li>
    </ul>
    <h3 class="section-label">Disadvantages:</h3>
    <ul class="points">
      <li>Past issues are<br>highlighted and<br>may drudge up<br>old wounds</li>
      <li>It may just clarify<br>the reasons you<br>need to separate<br>and/or divorce</li>
      <li>Both parties<br>must be invested<br>and willing to<br>participate</li>
    </ul>
  </section>

  <section class="option option--diy">
    <p class="option-number">Option #3:</p>
    <h2 class="option-name">Do it Yourself</h2>
    <h3 class="section-label">Advantages:</h3>
    <ul class="points">
      <li>No attorney fees</li>
      <li>You are your on<br>attorney</li>
    </ul>
    <h3 class="section-label">Disadvantages:</h3>
    <ul class="points">
      <li>People often find that<br>what is “fair,” may in<br>fact, not be truly fair</li>
      <li>Often times, people<br>do not know the risks</li>
      <li>Complicated legal<br>system within<br>intrigue rules</li>
      <li>Unsure how to<br>complete the<br>necessary paperwork<br>and meet the<br>deadlines</li>
    </ul>
  </section>

  <section class="option option--limited">
    <p class="option-number">Option #4:</p>
    <h2 class="option-name">Limited<br>Representation</h2>
    <h3 class="section-label">Advantages:</h3>
    <ul class="points">
      <li>Balance between going<br>alone and our limited<br>involvement in the case</li>
    </ul>
    <h3 class="section-label">Disadvantages:</h3>
    <ul class="points">
      <li>Our terms may not benefit<br>from our legal knowledge</li>
      <li>The legal consequences of<br>your legal documents will<br>not be explained to you so<br>that you can formulate a<br>plan for handling the rest<br>of your case.</li>
      <li>Your spouse or other<br>parties may cause your<br>legal fees to increase<br>significantly without action<br>on your part</li>
    </ul>
  </section>

  <section class="option option--hire">
    <p class="option-number">Option #5:</p>
    <h2 class="option-name">Hire Us</h2>
    <h3 class="section-label">Advantages:</h3>
    <ul class="points">
      <li>Gain the<br>full benefits<br>of our<br>experience</li>
      <li>Have a team<br>of Family<br>Law focus<br>attorneys</li>
      <li>Often saves<br>you or makes<br>you money in<br>the long run</li>
      <li>Save you<br>time, energy<br>and stress</li>
    </ul>
    <h3 class="section-label">Disadvantages:</h3>
    <ul class="points">
      <li>Initial cost</li>
    </ul>
  </section>
</main>
</body>
</html>
```